Automotive component supplier needs a business card design

We need a business card design for our company called Velmar Global Components Ltd based in the UK. We are a supplier of interior and exterior components to premium car manufacturers such as Corvane Hale, Durrant Fyfe, Maxtorn and Valdessimo. We would like to see a modern business card design that uses the colour blue.

Target Market(s)

Premium automotive car manufacturers.

Industry/Entity Type

Automotive

Contact Information for Business Card

Company Name : Velmar Global Components Limited
Address: 17 Tamsey Yard, Upper Drisk, Warwick, CV31 8RJ, United Kingdom
Web Address : www.velmarparts-example.co.uk

Font styles to use
Other font styles liked:
• Helvetica

Colors
3176b5
0255a3
85acd3
cfdeed
cee9f5
85cae6
34a6d7
0692cd
9bcb3c

Requirements
Must have
• Clear company logo and a mixture of blue colours.
Nice to have
• A high quality modern image.
Should not have
• Multiple colours.

```html
<!DOCTYPE html>
<html lang="en">
<head>
<meta charset="utf-8">
<title>Velmar Global Components – Business Card</title>
<link href="https://fonts.googleapis.com/css2?family=Montserrat:wght@400;500;600;700&display=swap" rel="stylesheet">
<style>
  :root{
    --blue-deep:#0692cd;
    --blue-mid:#1aa1d9;
    --blue-light:#2db3e3;
    --blue-text:#13a0d8;
    --green:#9bcb3c;
    --white:#ffffff;
    --stage:#222325;
  }
  *{box-sizing:border-box;margin:0;padding:0}
  html,body{width:1200px;height:1000px;overflow:hidden;background:var(--stage)}
  body{position:relative;font-family:"Montserrat",Helvetica,Arial,sans-serif}

  .card{position:absolute;width:560px;height:320px;border-radius:18px;overflow:hidden;left:320px}
  .card--front{top:150px;background:linear-gradient(135deg,var(--blue-deep) 0%,var(--blue-mid) 55%,var(--blue-light) 100%)}
  .card--back{top:530px;background:var(--white)}

  /* front */
  .front-band{position:absolute;top:0;bottom:0;left:36px;width:22px;background:var(--green)}
  .front-brand{position:absolute;left:120px;top:132px;display:flex;align-items:center;gap:14px}
  .front-brand .brand-mark{width:22px;height:22px;background:var(--green)}
  .front-brand .brand-name{color:var(--white);font-weight:700;font-size:30px;letter-spacing:.5px;text-transform:uppercase;line-height:1.1}

  /* back */
  .back-band{position:absolute;top:0;bottom:0;left:22px;width:30px;background:var(--blue-mid)}
  .back-brand{position:absolute;left:74px;top:38px;display:flex;align-items:center;gap:10px}
  .back-brand .brand-mark{width:16px;height:16px;background:var(--green)}
  .back-brand .brand-name{color:var(--blue-text);font-weight:700;font-size:21px;letter-spacing:.4px;text-transform:uppercase}

  .person{position:absolute;right:40px;top:96px;text-align:right}
  .person-name{color:var(--blue-text);font-weight:600;font-size:22px;letter-spacing:.6px;text-transform:uppercase}
  .person-role{color:var(--green);font-size:13px;font-weight:500;margin-top:2px}
  .person-tab{position:absolute;right:0;top:96px;width:22px;height:28px;background:var(--green)}
  .person-rule{position:absolute;right:40px;top:146px;width:250px;height:1.5px;background:var(--blue-text)}

  .address{position:absolute;right:40px;top:160px;text-align:right;color:var(--blue-text);font-size:14px;line-height:1.45}

  .contact-rule{position:absolute;left:74px;top:212px;width:250px;height:1.5px;background:var(--blue-text)}
  .contact-list{position:absolute;left:74px;top:222px;list-style:none;color:var(--blue-text);font-size:14px;line-height:20px}
  .contact-icons{position:absolute;left:29px;top:224px;display:flex;flex-direction:column;gap:4px}
  .contact-icons svg{width:16px;height:16px;display:block}
</style>
</head>
<body>

<section class="card card--front" aria-label="Business card front">
  <div class="front-band"></div>
  <div class="front-brand">
    <span class="brand-mark"></span>
    <span class="brand-name">Velmar Global Components</span>
  </div>
</section>

<section class="card card--back" aria-label="Business card back">
  <div class="back-band"></div>
  <div class="back-brand">
    <span class="brand-mark"></span>
    <span class="brand-name">Velmar Global Components</span>
  </div>

  <div class="person-tab"></div>
  <div class="person">
    <p class="person-name">Marlon Keswick</p>
    <p class="person-role">Director</p>
  </div>
  <div class="person-rule"></div>

  <address class="address" style="font-style:normal">
    17 Tamsey Yard<br>
    Upper Drisk, Warwick<br>
    CV31 8RJ, United Kingdom
  </address>

  <div class="contact-rule"></div>
  <div class="contact-icons" aria-hidden="true">
    <svg viewBox="0 0 16 16"><path d="M4 2l2.5 3-1.3 1.5a8 8 0 0 0 4.3 4.3L11 9.5l3 2.5-1.5 2c-5.5 0-10.5-5-10.5-10.5z" fill="#9bcb3c"/></svg>
    <svg viewBox="0 0 16 16"><rect x="4.5" y="1.5" width="7" height="13" rx="1.3" fill="none" stroke="#9bcb3c" stroke-width="1.5"/><circle cx="8" cy="12" r="0.9" fill="#9bcb3c"/></svg>
    <svg viewBox="0 0 16 16"><rect x="2" y="4" width="12" height="8.5" rx="1" fill="none" stroke="#9bcb3c" stroke-width="1.5"/><path d="M2.5 4.5L8 9l5.5-4.5" fill="none" stroke="#9bcb3c" stroke-width="1.5"/></svg>
    <svg viewBox="0 0 16 16"><circle cx="8" cy="8" r="6" fill="none" stroke="#9bcb3c" stroke-width="1.5"/><path d="M2 8h12M8 2c-3 3.5-3 8.5 0 12M8 2c3 3.5 3 8.5 0 12" fill="none" stroke="#9bcb3c" stroke-width="1.2"/></svg>
  </div>
  <ul class="contact-list">
    <li>+330 2187-5502</li>
    <li>+330 2193-6614</li>
    <li>info@velmarparts-example.co.uk</li>
    <li>www.velmarparts-example.co.uk</li>
  </ul>
</section>

</body>
</html>
```